Stationery for a private security company, "Tavrel Security Services Ltd."

Needed is a stationery design for a private security company. The designs must show professionalism and that our company mean nothing but business. Watermark of the company logo on the letterhead page is also a must. The final design must represent innovation and professionalism. It would be great if designers could integrate the colours black and silver onto the cards and letterheads..

Thank you

```html
<!DOCTYPE html>
<html lang="en">
<head>
<meta charset="utf-8">
<title>Tavrel Security Services Ltd. — Business Cards</title>
<link href="https://fonts.googleapis.com/css2?family=Cormorant+Garamond:wght@400;500&family=Lato:wght@300;400;700&display=swap" rel="stylesheet">
<style>
  :root {
    --stage: #2f2f30;
    --card-white: #ffffff;
    --card-black: #141414;
    --ink: #1a1a1a;
    --ink-soft: #3c3c3c;
    --silver: #c9c9cc;
    --silver-light: #ececee;
    --rule: #9a9a9a;
  }
  * { box-sizing: border-box; margin: 0; padding: 0; }
  html, body { width: 1200px; height: 781px; overflow: hidden; }
  body { background: var(--stage); position: relative; font-family: "Lato", sans-serif; }

  .card {
    position: absolute;
    width: 520px;
    height: 300px;
    border-radius: 22px;
    overflow: hidden;
  }

  .brand-mark { display: flex; align-items: center; gap: 10px; }
  .brand-mark__dot { width: 26px; height: 26px; border-radius: 50%; flex: none; }
  .brand-mark__name {
    font-family: "Lato", sans-serif; font-weight: 700;
    line-height: 1.2; text-transform: uppercase; letter-spacing: 0.5px;
  }

  /* Front card */
  .card--front { left: 50px; top: 240px; background: var(--card-white); }
  .front__brand { position: absolute; left: 34px; top: 0; height: 238px; width: 210px; display: flex; align-items: center; }
  .front__brand .brand-mark__dot { background: var(--ink); }
  .front__brand .brand-mark__name { color: var(--ink); font-size: 17px; }

  .front__divider {
    position: absolute; left: 258px; top: 40px; width: 1px; height: 160px; background: var(--rule);
  }
  .front__contact {
    position: absolute; left: 282px; top: 42px;
    font-family: "Cormorant Garamond", serif; color: var(--ink);
  }
  .contact__name { font-size: 22px; font-weight: 500; letter-spacing: 0.5px; text-transform: uppercase; }
  .contact__role { font-size: 14px; color: var(--ink-soft); margin-bottom: 18px; }
  .contact__line { font-size: 14px; line-height: 1.45; color: var(--ink-soft); }

  .front__band {
    position: absolute; left: 0; right: 0; bottom: 0; height: 62px; background: var(--card-black);
    display: flex; align-items: center; justify-content: center;
  }
  .site {
    font-family: "Lato", sans-serif; font-weight: 300; font-size: 14px;
    letter-spacing: 6px; color: var(--silver-light);
  }

  /* Back card */
  .card--back { left: 630px; top: 240px; background: var(--card-black); }
  .back__brand {
    position: absolute; left: 0; right: 0; top: 96px;
    justify-content: center; gap: 12px;
  }
  .back__brand .brand-mark__dot { background: var(--silver); }
  .back__brand .brand-mark__name { color: var(--silver); font-size: 20px; }
  .back__rule {
    position: absolute; left: 90px; right: 90px; bottom: 72px; height: 1px;
    background: linear-gradient(90deg, transparent, var(--silver), transparent);
  }
  .back__site { position: absolute; left: 0; right: 0; bottom: 40px; text-align: center; }
  .back__site .site { color: var(--silver); }
</style>
</head>
<body>
  <section class="card card--front" aria-label="Business card front">
    <div class="front__brand">
      <div class="brand-mark">
        <span class="brand-mark__dot"></span>
        <span class="brand-mark__name">Tavrel Security Services Ltd.</span>
      </div>
    </div>
    <div class="front__divider"></div>
    <div class="front__contact">
      <p class="contact__name">Mira Solberg</p>
      <p class="contact__role">Director / Founder</p>
      <p class="contact__line">your dummy address</p>
      <p class="contact__line">dummy city</p>
      <p class="contact__line">dummy zipcode</p>
      <p class="contact__line">+00 123 456 78910</p>
      <p class="contact__line">sales@tavrelsecurity.com</p>
    </div>
    <div class="front__band"><span class="site">www.tavrelsecurity.com</span></div>
  </section>

  <section class="card card--back" aria-label="Business card back">
    <div class="back__brand brand-mark">
      <span class="brand-mark__dot"></span>
      <span class="brand-mark__name">Tavrel Security Services Ltd.</span>
    </div>
    <div class="back__rule"></div>
    <div class="back__site"><span class="site">www.tavrelsecurity.com</span></div>
  </section>
</body>
</html>
```